New iOS App design for Boston Startup

We are looking for a new app design for our Zorvak app. The current app's design feels outdated and we like to add lots of new functionality and a new navigation as well. A complete overhaul therefore!
We want you to design 5 screens that will have changed the most. The complete wireframes of these 5 pages are attached in the requirements document.
Once the winning design is selected we will award the winner with the designing all other screens (40-50 screens based on the same design). This will be a separate project worth $1000. The winning designer can get more follow up work if both sides are happy about the cooperation.
We will give feedback as soon as the first screen has been uploaded for review. Final decision will be made only after all 5 screens are finished.
We hope you give it your best!
Note: will only communicate through PixelGuild (no skype),
Updates
Project Deadline Extended
Reason: Want to give designers a chance to submit their designs as I understand from some, the deadline is too close.
I have raised the award and introduced a 2nd price as well to make it worth your time. I hope you give it your best shot.
Project Deadline Extended
Reason: A few of you have asked for an extension of the deadline as time is running out. I will extend by one day. Tell me if you need more.
Industry/Entity Type
Startup
Requirements
Must have
- At least 1 screen before we can give you feedback.
Nice to have
- multiple options of 1 screen to get to a desirable design

```html
<!DOCTYPE html>
<html lang="en">
<head>
<meta charset="utf-8">
<title>Zorvak – Home</title>
<link rel="stylesheet" href="https://fonts.googleapis.com/css2?family=Inter:wght@400;500;600;700&display=swap">
<style>
  :root {
    --navy: #0f3452;
    --navy-dark: #0b2a44;
    --page: #f2f2f2;
    --card: #ffffff;
    --ink: #111111;
    --score-red: #d42027;
    --drop-pink: #ef7f7f;
    --gain-green: #3b7a17;
    --active-tab: #00b4ee;
    --white: #ffffff;
  }
  * { box-sizing: border-box; margin: 0; padding: 0; }
  html, body { width: 800px; height: 1200px; overflow: hidden; }
  body {
    font-family: "Inter", "Helvetica Neue", Arial, sans-serif;
    background: var(--page);
    color: var(--ink);
    position: relative;
  }
  .status-bar {
    position: absolute; left: 0; top: 0; width: 800px; height: 50px;
    background: var(--navy); color: var(--white);
    font-size: 25px; font-weight: 500;
  }
  .status-bar .carrier { position: absolute; left: 10px; top: 10px; display: flex; align-items: center; gap: 6px; }
  .signal { display: flex; gap: 3px; margin-right: 4px; }
  .signal i { width: 10px; height: 10px; border-radius: 50%; border: 1.5px solid var(--white); display: block; }
  .signal i.on { background: var(--white); }
  .status-bar .clock { position: absolute; left: 0; width: 800px; text-align: center; top: 10px; }
  .status-bar .right { position: absolute; right: 10px; top: 10px; display: flex; align-items: center; gap: 10px; }
  .battery { width: 50px; height: 22px; border: 2px solid var(--white); border-radius: 4px; padding: 2px; position: relative; }
  .battery::before { content: ""; display: block; width: 100%; height: 100%; background: var(--white); border-radius: 1px; }
  .battery::after { content: ""; position: absolute; right: -6px; top: 5px; width: 3px; height: 8px; background: var(--white); border-radius: 0 2px 2px 0; }

  .app-header {
    position: absolute; left: 0; top: 50px; width: 800px; height: 110px;
    background: var(--navy); color: var(--white);
  }
  .menu-button { position: absolute; left: 30px; top: 34px; width: 52px; height: 40px; }
  .menu-button span { display: block; height: 6px; background: var(--white); border-radius: 3px; margin-bottom: 11px; }
  .app-header h1 { text-align: center; font-size: 40px; font-weight: 700; line-height: 110px; letter-spacing: -0.3px; }

  .score-card {
    position: absolute; left: 30px; top: 178px; width: 170px; height: 162px;
    background: var(--card); border-radius: 8px; overflow: hidden; text-align: center;
  }
  .score-card .label { background: var(--navy); color: var(--white); font-size: 32px; font-weight: 500; height: 47px; line-height: 47px; letter-spacing: 1px; }
  .score-card .value { color: var(--score-red); font-size: 80px; font-weight: 500; line-height: 82px; letter-spacing: -3px; }
  .score-card .delta { color: var(--drop-pink); font-size: 23px; line-height: 26px; }

  .weekly-stats {
    position: absolute; left: 229px; top: 178px; width: 536px; height: 100px;
    border: 2px solid var(--navy); border-radius: 8px; overflow: hidden;
    display: grid; grid-template-columns: 175px 186px 1fr;
  }
  .stat { display: flex; flex-direction: column; }
  .stat + .stat { border-left: 2px solid var(--navy); }
  .stat .figure { height: 66px; background: var(--card); display: flex; align-items: center; justify-content: center; font-size: 37px; }
  .stat .gain { color: var(--gain-green); font-size: 24px; margin-left: 2px; display: flex; align-items: center; }
  .stat .gain svg { width: 14px; height: 24px; margin-right: 2px; }
  .stat .caption { flex: 1; background: var(--navy); color: var(--white); font-size: 25px; text-align: center; line-height: 30px; }

  .week-switch { position: absolute; left: 360px; top: 296px; width: 276px; height: 40px; display: flex; align-items: center; justify-content: space-between; }
  .week-switch .arrow { width: 44px; height: 40px; background: var(--navy); display: flex; align-items: center; justify-content: center; }
  .week-switch .period { color: var(--navy); font-size: 28px; font-weight: 700; letter-spacing: 0.5px; }

  .nav-card {
    position: absolute; left: 20px; width: 760px; height: 109px;
    background: var(--card); border-top: 7px solid var(--ink); border-radius: 8px;
    display: flex; align-items: center; font-size: 42px; font-weight: 500;
  }
  .nav-card .icon { width: 86px; display: flex; justify-content: center; }
  .nav-card .days { font-size: 46px; font-weight: 700; }
  .nav-card .chevron { position: absolute; right: 20px; top: 34px; }
  .analytics { top: 406px; }
  .overview { top: 559px; }
  .countdown { top: 704px; }

  .next-lesson { position: absolute; left: 246px; top: 888px; width: 298px; height: 81px; }
  .next-lesson span { position: absolute; left: 22px; top: 0; line-height: 81px; color: var(--white); font-size: 37px; font-weight: 500; }

  .tab-bar { position: absolute; left: 0; top: 1078px; width: 800px; height: 122px; background: var(--navy); display: flex; }
  .tab { width: 160px; display: flex; flex-direction: column; align-items: center; color: var(--white); font-size: 24px; font-weight: 600; padding-top: 16px; }
  .tab svg { height: 70px; margin-bottom: 8px; }
  .tab.active { background: var(--active-tab); width: 150px; margin-top: -9px; padding-top: 25px; }
  .tab.theory { width: 165px; }
  .tab.practice { width: 160px; }
  .tab.games { width: 165px; }
</style>
</head>
<body>
  <div class="status-bar">
    <div class="carrier"><span class="signal"><i class="on"></i><i class="on"></i><i class="on"></i><i></i><i></i></span>Velnet
      <svg width="28" height="22" viewBox="0 0 28 22"><path d="M2 8 A16 16 0 0 1 26 8" stroke="#fff" stroke-width="3" fill="none"/><path d="M7 13 A10 10 0 0 1 21 13" stroke="#fff" stroke-width="3" fill="none"/><circle cx="14" cy="18" r="3" fill="#fff"/></svg>
    </div>
    <div class="clock">23:12</div>
    <div class="right">
      <svg width="16" height="26" viewBox="0 0 16 26"><path d="M2 7 L14 19 L8 24 L8 2 L14 7 L2 19" stroke="#fff" stroke-width="2" fill="none"/></svg>
      <span>100%</span><span class="battery"></span>
    </div>
  </div>

  <header class="app-header">
    <div class="menu-button"><span></span><span></span><span></span></div>
    <h1>Welcome back, Arin</h1>
  </header>

  <section class="score-card">
    <div class="label">SCORE</div>
    <div class="value">650</div>
    <div class="delta">↓-18</div>
  </section>

  <section class="weekly-stats">
    <div class="stat"><div class="figure">34%<span class="gain"><svg viewBox="0 0 14 24"><path d="M7 2 L13 11 L9 11 L9 22 L5 22 L5 11 L1 11 Z" fill="#3b7a17"/></svg>+10</span></div><div class="caption">completion</div></div>
    <div class="stat"><div class="figure">20<span class="gain"><svg viewBox="0 0 14 24"><path d="M7 2 L13 11 L9 11 L9 22 L5 22 L5 11 L1 11 Z" fill="#3b7a17"/></svg>+3</span></div><div class="caption">sessions</div></div>
    <div class="stat"><div class="figure">18<span class="gain"><svg viewBox="0 0 14 24"><path d="M7 2 L13 11 L9 11 L9 22 L5 22 L5 11 L1 11 Z" fill="#3b7a17"/></svg>+10</span></div><div class="caption">min.</div></div>
  </section>

  <div class="week-switch">
    <span class="arrow"><svg width="14" height="22" viewBox="0 0 14 22"><path d="M11 2 L3 11 L11 20" stroke="#fff" stroke-width="3.5" fill="none"/></svg></span>
    <span class="period">THIS WEEK</span>
    <span class="arrow"><svg width="14" height="22" viewBox="0 0 14 22"><path d="M3 2 L11 11 L3 20" stroke="#fff" stroke-width="3.5" fill="none"/></svg></span>
  </div>

  <a class="nav-card analytics">
    <span class="icon"><svg width="48" height="38" viewBox="0 0 48 38"><rect x="1" y="1" width="46" height="36" fill="none" stroke="#111" stroke-width="2"/><path d="M6 30 L16 18 L24 24 L38 10 M33 10 L38 10 L38 15" fill="none" stroke="#111" stroke-width="2"/></svg></span>
    Analytics
    <svg class="chevron" width="20" height="34" viewBox="0 0 20 34"><path d="M3 3 L16 17 L3 31" stroke="#111" stroke-width="4" fill="none"/></svg>
  </a>
  <a class="nav-card overview">
    <span class="icon"><svg width="48" height="38" viewBox="0 0 48 38"><g fill="none" stroke="#111" stroke-width="2"><circle cx="5" cy="5" r="3.5"/><circle cx="5" cy="19" r="3.5"/><circle cx="5" cy="33" r="3.5"/><path d="M14 5 H46 M14 14 H46 M14 24 H46 M14 33 H46"/></g></svg></span>
    Course Overview
    <svg class="chevron" width="20" height="34" viewBox="0 0 20 34"><path d="M3 3 L16 17 L3 31" stroke="#111" stroke-width="4" fill="none"/></svg>
  </a>
  <a class="nav-card countdown">
    <span class="icon days">33</span>
    Days until test
    <svg class="chevron" width="20" height="34" viewBox="0 0 20 34"><path d="M3 3 L16 17 L3 31" stroke="#111" stroke-width="4" fill="none"/></svg>
  </a>

  <a class="next-lesson">
    <svg width="298" height="81" viewBox="0 0 298 81"><path d="M6 0 H254 L298 40.5 L254 81 H6 Q0 81 0 75 V6 Q0 0 6 0 Z" fill="#0f3452"/></svg>
    <span>Next Lesson</span>
  </a>

  <nav class="tab-bar">
    <div class="tab theory"><svg viewBox="0 0 54 70" width="54"><g fill="none" stroke="#fff" stroke-width="3"><rect x="4" y="4" width="46" height="62"/><path d="M10 4 V66"/></g></svg>Theory</div>
    <div class="tab practice"><svg viewBox="0 0 70 70" width="70"><g fill="none" stroke="#fff" stroke-width="3"><path d="M52 6 L64 18 L24 58 L8 64 L12 48 Z M12 48 L24 58 M46 12 L58 24"/></g></svg>Practice</div>
    <div class="tab active"><svg viewBox="0 0 70 70" width="70"><path d="M35 6 L66 36 H58 V66 H42 V46 H28 V66 H12 V36 H4 Z" fill="#fff"/><rect x="48" y="10" width="8" height="16" fill="#fff"/></svg>Home</div>
    <div class="tab games"><svg viewBox="0 0 60 70" width="60"><g fill="none" stroke="#fff" stroke-width="3"><circle cx="30" cy="12" r="6"/><path d="M30 18 V46"/><rect x="4" y="46" width="52" height="16" rx="2"/><path d="M14 46 V40 H22 V46"/></g></svg>Games</div>
    <div class="tab"><svg viewBox="0 0 54 70" width="54"><g fill="none" stroke="#fff" stroke-width="3"><path d="M4 4 H36 L50 18 V66 H4 Z M36 4 V18 H50"/><path d="M12 28 H42 M12 36 H42 M12 44 H42 M12 52 H42"/></g></svg>Test</div>
  </nav>
</body>
</html>
```